Kovrix - consultancy website

I need a new design for my webpage/presence [to be functioning with Wordpress - I have a programmer to set it up but not the design idea].
My company is Kovrix - a consultancy firm focused on growth management for Swedish SME's primarily;. We call it Leadership add-on for firms on the rise, kind of a doctor helping small become big. Contentwise, its a simple frontpage + 3-4 subpages with content re company/myself/focus etc. The new site should communicate a fresh, trustworthy take yet simple and functional on all devices [i.e. think UI compatible for mobile/tablet]. Current building parts/form elements are
a) existing logo and text elements
b) existing pictures
c) the yellowish color
colours and new ideas on pictures/positioning are welcome. I prefer a 'full width page' solution with centralised text elements but that's all up to you to suggest. Current site is a quickfix made by myself - now I'm moving it to a new platform so want to take the opportunity to make it
Nothing superspecial as it is a 2-man show; on the other hand I still want to have a modern & fresh reflection of my brand in digital environments. Help me out!
www.kovrix-demo.se
Best
Lotta Bergqvalm

```html
<!DOCTYPE html>
<html lang="en">
<head>
<meta charset="utf-8">
<title>Kovrix – Leadership add-on for firms on the rise</title>
<link rel="stylesheet" href="https://fonts.googleapis.com/css2?family=Libre+Baskerville&family=Montserrat:wght@400;600;700&family=Open+Sans:wght@400;600&display=swap">
<style>
  :root {
    --white: #ffffff;
    --ink: #222222;
    --text-grey: #777777;
    --line-grey: #d6d6d6;
    --dark: #1d1d1d;
    --dark-band: #191919;
    --footer: #1f1f1f;
    --footer-text: #9a9a9a;
    --icon-fill: #d4d4d4;
    --accent: #f5a623;
    --hero-top: #d8b86a;
    --hero-mid: #a8844a;
    --hero-low: #5e4a30;
    --red: #c01f2d;
    --red-light: #d8414d;
  }
  * { box-sizing: border-box; margin: 0; padding: 0; }
  html, body { width: 1200px; height: 2228px; overflow: hidden; }
  body { position: relative; background: var(--white); font-family: "Open Sans", Arial, sans-serif; color: var(--ink); }

  .site-header { position: absolute; top: 0; left: 0; width: 1200px; height: 72px; background: var(--white); display: flex; align-items: center; justify-content: space-between; padding: 0 40px 0 48px; }
  .brand { font-family: "Libre Baskerville", Georgia, serif; font-size: 30px; color: var(--ink); }
  .main-nav { display: flex; gap: 30px; font-family: "Montserrat", Arial, sans-serif; font-size: 11px; font-weight: 600; letter-spacing: 0.5px; }

  .hero { position: absolute; top: 72px; left: 0; width: 1200px; height: 588px;
    background: linear-gradient(180deg, var(--hero-top) 0%, var(--hero-mid) 45%, var(--hero-low) 100%); color: var(--white); text-align: center; }
  .hero-kicker { position: absolute; top: 176px; width: 100%; font-family: "Montserrat", Arial, sans-serif; font-size: 42px; letter-spacing: 2px; color: rgba(255,255,255,0.75); }
  .hero-title { position: absolute; top: 242px; width: 100%; font-family: "Montserrat", Arial, sans-serif; font-size: 32px; font-weight: 700; letter-spacing: 1px; }
  .hero-lead { position: absolute; top: 300px; left: 370px; width: 460px; font-size: 13px; line-height: 20px; }
  .btn-dark { position: absolute; top: 410px; left: 540px; width: 120px; height: 36px; border-radius: 18px; background: var(--dark); color: var(--white); font-size: 12px; font-weight: 600; line-height: 36px; }

  .cta-band { position: absolute; top: 660px; left: 0; width: 1200px; height: 112px; background: var(--dark-band); color: var(--white); }
  .cta-band p { position: absolute; top: 47px; left: 300px; font-size: 13px; }
  .btn-accent { position: absolute; top: 43px; left: 800px; width: 130px; height: 26px; border-radius: 13px; background: var(--accent); color: var(--white); font-size: 12px; font-weight: 600; text-align: center; line-height: 26px; }

  .section-title { position: absolute; top: 870px; width: 100%; text-align: center; font-family: "Montserrat", Arial, sans-serif; font-size: 22px; font-weight: 400; letter-spacing: 0.5px; }
  .section-title strong { font-weight: 700; }

  .timeline-line { position: absolute; top: 970px; left: 599px; width: 2px; height: 720px; background: var(--line-grey); }
  .timeline-dot { position: absolute; left: 590px; width: 20px; height: 20px; border-radius: 50%; background: var(--white); border: 2px solid var(--line-grey); }
  .timeline-dot.is-active { border-color: var(--accent); }
  .timeline-dot.is-active::after { content: ""; position: absolute; left: 4px; top: 4px; width: 8px; height: 8px; border-radius: 50%; background: var(--accent); }
  .timeline-tick { position: absolute; left: 596px; top: 1010px; width: 8px; height: 8px; border-radius: 50%; background: var(--accent); }

  .platform-item { position: absolute; width: 270px; }
  .platform-item h3 { font-family: "Montserrat", Arial, sans-serif; font-size: 14px; font-weight: 700; margin-bottom: 10px; }
  .platform-item p { font-size: 11px; line-height: 17px; color: var(--text-grey); }
  .platform-note { position: absolute; top: 1790px; left: 652px; width: 320px; font-size: 10px; line-height: 15px; color: var(--text-grey); }

  .illustration { position: absolute; border-radius: 50%; background: radial-gradient(circle at 40% 35%, var(--red-light) 0%, var(--red) 70%); }

  .site-footer { position: absolute; top: 1988px; left: 0; width: 1200px; height: 240px; background: var(--footer); color: var(--footer-text); font-size: 11px; }
  .footer-brand { position: absolute; top: 80px; left: 100px; font-family: "Libre Baskerville", Georgia, serif; font-size: 36px; color: var(--footer-text); }
  .footer-col { position: absolute; top: 72px; }
  .footer-col h4 { font-family: "Montserrat", Arial, sans-serif; font-size: 13px; font-weight: 600; color: #cfcfcf; letter-spacing: 0.5px; margin-bottom: 14px; }
  .footer-divider { position: absolute; top: 72px; width: 1px; height: 90px; background: #3a3a3a; }
  .social-list { display: flex; gap: 8px; }
  .social-list span { width: 24px; height: 24px; border-radius: 3px; background: var(--icon-fill); display: block; }
  .signup-field { width: 200px; height: 26px; background: #3a3a3a; border-radius: 2px; padding: 0 10px; line-height: 26px; font-size: 10px; color: #888; }
  .contact-grid { display: grid; grid-template-columns: 130px 150px; row-gap: 4px; font-size: 10px; }
  .contact-grid .accent { color: var(--accent); }
  .footer-copy { position: absolute; top: 212px; width: 100%; text-align: center; font-size: 9px; color: #666; }
</style>
</head>
<body>
  <header class="site-header">
    <div class="brand">Kovrix.</div>
    <nav class="main-nav"><span>HOME</span><span>PLATFORM</span><span>CONTACT</span></nav>
  </header>

  <section class="hero" role="img" aria-label="Golden-hour photo of a coastal city skyline with harbour and ships">
    <div class="hero-kicker">LOREM IPSUM</div>
    <h1 class="hero-title">MOBILE ROBOTIC INTEGRATION</h1>
    <p class="hero-lead">Lorem ipsum dolor sit amet, consectetur adipiscing elit. Aenean commodo ligula eget dolor. Aenean massa. Cum sociis natoque.</p>
    <div class="btn-dark">Learn More</div>
  </section>

  <section class="cta-band">
    <p>Lorem ipsum dolor sit amet, consectetur adipiscing elit.</p>
    <div class="btn-accent">Inquire</div>
  </section>

  <h2 class="section-title">THE <strong>PLATFORM</strong></h2>

  <div class="timeline-line"></div>
  <div class="timeline-dot is-active" style="top:972px"></div>
  <div class="timeline-tick"></div>
  <div class="timeline-dot" style="top:1312px"></div>
  <div class="timeline-dot" style="top:1642px"></div>

  <div class="illustration" role="img" aria-label="Illustration of a stopwatch, monitor with bar chart and robot icon on a red circle" style="top:950px;left:210px;width:210px;height:210px"></div>
  <article class="platform-item" style="top:972px;left:652px">
    <h3>What we do</h3>
    <p>Lorem ipsum dolor sit amet, consectetur adipiscing elit. Aenean commodo ligula eget dolor. Aenean massa cum sociis natoque penatibus et magnis dis parturient montes, nascetur ridiculus mus. Donec quam felis.</p>
  </article>

  <article class="platform-item" style="top:1310px;left:220px">
    <h3>Who we are</h3>
    <p>Lorem ipsum dolor sit amet, consectetur adipiscing elit. Aenean commodo ligula eget dolor. Aenean massa cum sociis natoque penatibus et magnis dis parturient montes, nascetur ridiculus mus. Donec quam felis.</p>
  </article>
  <div class="illustration" role="img" aria-label="Illustration of a box sending wifi, document and chip icons upward" style="top:1330px;left:690px;width:200px;height:200px"></div>

  <div class="illustration" role="img" aria-label="Illustration of a satellite above three red circles with devices" style="top:1620px;left:200px;width:230px;height:230px"></div>
  <article class="platform-item" style="top:1638px;left:652px">
    <h3>Why we</h3>
    <p>Lorem ipsum dolor sit amet, consectetur adipiscing elit. Aenean commodo ligula eget dolor. Aenean massa cum sociis natoque penatibus et magnis dis parturient montes, nascetur ridiculus mus. Donec quam felis.</p>
  </article>
  <p class="platform-note">Leadership add-on for firms on the rise, helping small become big.</p>

  <footer class="site-footer">
    <div class="footer-brand">Kovrix.</div>
    <div class="footer-col" style="left:310px">
      <h4>CONNECT</h4>
      <div class="social-list" aria-label="Social links"><span></span><span></span><span></span></div>
    </div>
    <div class="footer-divider" style="left:470px"></div>
    <div class="footer-col" style="left:505px">
      <h4>SIGN UP AND RECEIVE UPDATES</h4>
      <div class="signup-field">Email address</div>
    </div>
    <div class="footer-divider" style="left:760px"></div>
    <div class="footer-col" style="left:790px">
      <h4>CONTACT US</h4>
      <div class="contact-grid">
        <span>Storgatan 12</span><span class="accent">+46 70 000 00 00</span>
        <span>111 22 Stockholm</span><span class="accent">www.kovrix-demo.se</span>
        <span>Sweden</span><span>Lotta Bergqvalm</span>
      </div>
    </div>
    <div class="footer-copy">© 2024 Kovrix. All rights reserved.</div>
  </footer>
</body>
</html>
```